Brightmoor Notes To Do List

I am looking to design a new "Study To Do List" for High School students (Ages 15 - 18) . This will be printed as an A4 notepad and so should only be a single A4 page.

The Design will need to be professional and look semi-serious but also be appealing to High school students (Ages 15 - 18) and should NOT be gender specific.

I have attached a word document outlining the structure of the page. The space provided should be large enough that people can write in it comfortably.

The notepad will most likely be printed in black and white but I'm also looking at coloured options - colours should be kept to a minimum.

This will be printed professionally and should also include a 3mm bleed.

The design should also include the business logo (included in the word document)

Target Market(s)

High School students (Ages 15 - 18). Both genders

Industry/Entity Type

Education

Font styles to use
Serif
Sans Serif

Requirements
Must have
• Please see the word document attached.
Should not have
• Too much colour

```html
<!DOCTYPE html>
<html lang="en">
<head>
<meta charset="utf-8">
<title>Brightmoor Notes To Do List</title>
<link rel="stylesheet" href="https://fonts.googleapis.com/css2?family=Roboto+Condensed:wght@400;700&display=swap">
<style>
  :root {
    --navy: #1f2f45;
    --orange: #f47a20;
    --bar: #dcdce0;
    --rule: #5a6472;
    --entry: #7a7f88;
    --paper: #ffffff;
    --backdrop: #e9e7e3;
  }
  html, body { margin: 0; width: 1200px; height: 1200px; overflow: hidden; background: var(--backdrop); }
  body { font-family: "Roboto Condensed", sans-serif; color: var(--navy); }
  .sheet {
    position: absolute; left: 152px; top: 20px;
    width: 959px; height: 1242px; background: var(--paper);
    transform: scale(0.934); transform-origin: top left;
    box-shadow: 0 4px 18px rgba(0,0,0,.18);
  }
  .sheet > * { position: absolute; }
  .header-art-left {
    left: 0; top: 0; width: 130px; height: 175px;
    background: linear-gradient(180deg, var(--navy) 0%, var(--navy) 38%, var(--orange) 62%, var(--orange) 100%);
  }
  .header-art-right {
    left: 345px; top: 100px; width: 560px; height: 46px;
    background: linear-gradient(90deg, var(--navy) 0%, var(--orange) 100%);
  }
  .brand { left: 150px; top: 118px; display: flex; align-items: center; gap: 10px; }
  .brand-dot { width: 22px; height: 22px; border-radius: 50%; background: var(--navy); flex: none; }
  .brand-name { font-weight: 700; font-size: 22px; color: var(--navy); line-height: 1.05; }
  .title { left: 262px; top: 38px; font-size: 37px; font-weight: 700; margin: 0; letter-spacing: .2px; }
  .label { font-size: 18px; color: var(--navy); }
  .entry { font-size: 17px; color: var(--entry); }
  .date-label { left: 744px; top: 160px; font-size: 25px; font-weight: 700; border-bottom: 2px solid var(--navy); line-height: 1; padding-bottom: 1px; }
  .date-line { left: 805px; top: 186px; width: 129px; border-bottom: 1px solid var(--rule); }
  .date-value { left: 810px; top: 164px; }
  .name-label { left: 514px; top: 222px; font-size: 24px; font-weight: 700; }
  .name-value { left: 593px; top: 216px; font-size: 31px; color: var(--entry); }
  .heading { font-size: 37px; font-weight: 700; margin: 0; line-height: 1; }
  .bar { background: var(--bar); height: 28px; }
  .rule { border-bottom: 1px solid var(--rule); height: 0; }
  .row { display: flex; align-items: flex-end; font-size: 17px; height: 24px; }
  .row .num { color: var(--navy); width: 25px; }
  .row .val { color: var(--entry); }
  sup { font-size: 9px; }
</style>
</head>
<body>
<main class="sheet">
  <div class="header-art-left" role="img" aria-label="Decorative navy and orange header bands"></div>
  <div class="header-art-right" role="img" aria-label="Decorative navy and orange sweeping header band"></div>

  <div class="brand">
    <span class="brand-dot"></span>
    <span class="brand-name">Halden Academy</span>
  </div>

  <h1 class="title">BRIGHTMOOR NOTES TO DO LIST</h1>

  <span class="date-label">DATE</span>
  <span class="date-value entry">1<sup>ST</sup> JUNE 2017</span>
  <span class="date-line"></span>

  <span class="name-label">NAME</span>
  <span class="name-value">MY NAME HERE...</span>

  <h2 class="heading" style="left:42px;top:248px">REVISION</h2>
  <div class="bar" style="left:325px;top:255px;width:609px"></div>
  <div class="row" style="left:42px;top:294px"><span class="num">1.</span><span class="val">MATHS</span></div>
  <div class="row" style="left:42px;top:328px"><span class="num">2.</span><span class="val">EINGLISH</span></div>
  <div class="row" style="left:42px;top:362px"><span class="num">3.</span><span class="val">HISTORY</span></div>
  <div class="row" style="left:344px;top:294px"><span class="num">4.</span><span class="val">MATHS</span></div>
  <div class="row" style="left:344px;top:328px"><span class="num">5.</span><span class="val">EINGLISH</span></div>
  <div class="row" style="left:344px;top:362px"><span class="num">6.</span><span class="val">HISTORY</span></div>
  <div class="row" style="left:685px;top:294px"><span class="num">7.</span><span class="val">MATHS</span></div>
  <div class="row" style="left:685px;top:328px"><span class="num">8.</span><span class="val">EINGLISH</span></div>
  <div class="row" style="left:685px;top:362px"><span class="num">9.</span><span class="val">HISTORY</span></div>
  <div class="rule" style="left:36px;top:317px;width:286px"></div>
  <div class="rule" style="left:36px;top:352px;width:286px"></div>
  <div class="rule" style="left:36px;top:386px;width:286px"></div>
  <div class="rule" style="left:338px;top:317px;width:322px"></div>
  <div class="rule" style="left:338px;top:352px;width:322px"></div>
  <div class="rule" style="left:338px;top:386px;width:322px"></div>
  <div class="rule" style="left:677px;top:317px;width:257px"></div>
  <div class="rule" style="left:677px;top:352px;width:257px"></div>
  <div class="rule" style="left:677px;top:386px;width:257px"></div>

  <h2 class="heading" style="left:43px;top:423px">HOMEWORK</h2>
  <div class="bar" style="left:325px;top:428px;width:609px"></div>
  <span class="label" style="left:44px;top:467px">SUBJECT</span>
  <span class="label" style="left:342px;top:467px">TASK</span>
  <div class="rule" style="left:36px;top:491px;width:286px"></div>
  <div class="rule" style="left:339px;top:491px;width:595px"></div>
  <span class="entry" style="left:45px;top:508px">MATHS</span>
  <span class="entry" style="left:45px;top:541px">EINGLISH</span>
  <span class="entry" style="left:45px;top:574px">HISTORY</span>
  <span class="entry" style="left:45px;top:607px">SOCIAL SIC</span>
  <span class="entry" style="left:341px;top:508px">HOME WORK LESSONE NO 1 TO 5</span>
  <span class="entry" style="left:341px;top:540px">HOME WORK LESSONE NO 1 TO 5</span>
  <span class="entry" style="left:341px;top:572px">HOME WORK LESSONE NO 1 TO 5</span>
  <span class="entry" style="left:341px;top:608px">HOME WORK LESSONE NO 1 TO 5</span>
  <div class="rule" style="left:36px;top:527px;width:286px"></div>
  <div class="rule" style="left:36px;top:560px;width:286px"></div>
  <div class="rule" style="left:36px;top:593px;width:286px"></div>
  <div class="rule" style="left:36px;top:628px;width:286px"></div>
  <div class="rule" style="left:36px;top:662px;width:286px"></div>
  <div class="rule" style="left:36px;top:694px;width:286px"></div>
  <div class="rule" style="left:36px;top:729px;width:286px"></div>
  <div class="rule" style="left:36px;top:762px;width:286px"></div>
  <div class="rule" style="left:339px;top:527px;width:595px"></div>
  <div class="rule" style="left:339px;top:560px;width:595px"></div>
  <div class="rule" style="left:339px;top:593px;width:595px"></div>
  <div class="rule" style="left:339px;top:628px;width:595px"></div>
  <div class="rule" style="left:339px;top:662px;width:595px"></div>
  <div class="rule" style="left:339px;top:694px;width:595px"></div>
  <div class="rule" style="left:339px;top:729px;width:595px"></div>
  <div class="rule" style="left:339px;top:762px;width:595px"></div>

  <h2 class="heading" style="left:42px;top:796px">ASSESSMENTS</h2>
  <div class="bar" style="left:325px;top:800px;width:609px"></div>

  <span class="label" style="left:42px;top:840px">ASSESSMENT</span>
  <span class="entry" style="left:160px;top:841px">MATHS, &nbsp;EINGLISH, HISTORY</span>
  <span class="label" style="left:571px;top:840px">DUE</span>
  <span class="entry" style="left:617px;top:841px">15<sup>TH</sup> JUNE 2017</span>
  <div class="rule" style="left:36px;top:862px;width:513px"></div>
  <div class="rule" style="left:571px;top:862px;width:363px"></div>
  <span class="label" style="left:42px;top:876px">ELEMENT</span>
  <span class="entry" style="left:160px;top:876px">NOOTBOOK OTHER ELEMENTS USING</span>
  <div class="rule" style="left:36px;top:897px;width:898px"></div>

  <span class="label" style="left:42px;top:908px">ASSESSMENT</span>
  <span class="entry" style="left:160px;top:909px">MATHS, &nbsp;EINGLISH, HISTORY</span>
  <span class="label" style="left:571px;top:909px">DUE</span>
  <span class="entry" style="left:617px;top:909px">15<sup>TH</sup> JUNE 2017</span>
  <div class="rule" style="left:36px;top:930px;width:513px"></div>
  <div class="rule" style="left:571px;top:930px;width:363px"></div>
  <span class="label" style="left:42px;top:944px">ELEMENT</span>
  <div class="rule" style="left:36px;top:963px;width:898px"></div>

  <span class="label" style="left:42px;top:978px">ASSESSMENT</span>
  <span class="entry" style="left:160px;top:979px">MATHS, &nbsp;EINGLISH, HISTORY</span>
  <span class="label" style="left:571px;top:978px">DUE</span>
  <span class="entry" style="left:617px;top:979px">15<sup>TH</sup> JUNE 2017</span>
  <div class="rule" style="left:36px;top:998px;width:513px"></div>
  <div class="rule" style="left:571px;top:998px;width:363px"></div>
  <span class="label" style="left:42px;top:1011px">ELEMENT</span>
  <div class="rule" style="left:36px;top:1031px;width:898px"></div>

  <h2 class="heading" style="left:42px;top:1050px;font-size:29px">NOTES</h2>
  <div class="bar" style="left:265px;top:1052px;width:284px"></div>
  <div class="rule" style="left:36px;top:1080px;width:513px"></div>
  <div class="row" style="left:47px;top:1092px"><span class="num" style="width:20px">1.</span><span class="val">NOOTBOOK OTHER</span></div>
  <div class="row" style="left:47px;top:1127px"><span class="num">2.</span></div>
  <div class="row" style="left:47px;top:1161px"><span class="num">3.</span></div>
  <div class="row" style="left:317px;top:1092px"><span class="num">4.</span></div>
  <div class="row" style="left:317px;top:1127px"><span class="num">5.</span></div>
  <div class="row" style="left:317px;top:1161px"><span class="num">6.</span></div>
  <div class="rule" style="left:36px;top:1116px;width:264px"></div>
  <div class="rule" style="left:36px;top:1149px;width:264px"></div>
  <div class="rule" style="left:36px;top:1183px;width:264px"></div>
  <div class="rule" style="left:311px;top:1116px;width:238px"></div>
  <div class="rule" style="left:311px;top:1149px;width:238px"></div>
  <div class="rule" style="left:311px;top:1183px;width:238px"></div>

  <h2 class="heading" style="left:572px;top:1050px;font-size:29px">PRACTICE</h2>
  <div class="bar" style="left:704px;top:1052px;width:230px"></div>
  <div class="rule" style="left:571px;top:1080px;width:363px"></div>
  <span class="entry" style="left:577px;top:1093px">MATHS, &nbsp;EINGLISH, HISTORY</span>
  <div class="rule" style="left:571px;top:1116px;width:363px"></div>
  <div class="rule" style="left:571px;top:1149px;width:363px"></div>
  <div class="rule" style="left:571px;top:1183px;width:363px"></div>
</main>
</body>
</html>
```